Delvin & Associates - London New Letting and Property Management Company *

Delvin & Associates LTD is a new company based in London, and works with brand new residential property in the city centre.

We are aiming to have 1000 new properties a year.

We are looking for something modern and minimalistic :
Logo ,Monogram, Paper Head and Business Card.

Target Market(s)

Internation landlords

Industry/Entity Type

Real Estate

Logo Text

Delvin & Associates

Colors

Designer to choose colors to be used in the design.

Requirements
Nice to have
• A particular monogram with "DA"
Should not have
• Little House over the logo

```html
<!DOCTYPE html>
<html lang="en">
<head>
<meta charset="utf-8">
<title>Delvin &amp; Associates — Brand Stationery</title>
<link href="https://fonts.googleapis.com/css2?family=Bodoni+Moda:wght@400&family=Lato:wght@400;700&display=swap" rel="stylesheet">
<style>
  :root{
    --board:#e4e4e6;
    --ink:#2b2b2b;
    --charcoal:#3a3a3b;
    --black:#000;
    --paper:#fff;
    --muted:#707070;
    --rule:#9a9a9a;
    --kraft:#b49a78;
  }
  *{box-sizing:border-box;margin:0;padding:0}
  html,body{width:1200px;height:1200px;overflow:hidden}
  body{background:var(--board);position:relative;font-family:"Lato",sans-serif;color:var(--ink)}
  .piece{position:absolute}

  /* Company name set as plain text where the mark stands */
  .brand-name{position:absolute;text-align:center;font-family:"Bodoni Moda",serif;font-weight:400;
    color:var(--ink);font-size:var(--s);line-height:1.1;letter-spacing:0.02em;white-space:nowrap;text-transform:uppercase}
  .brand-name.on-dark{color:var(--paper)}

  /* Top row */
  .brand-light{left:0;top:124px;width:374px;--s:21px}
  .brand-dark{left:374px;top:0;width:380px;height:240px;background:var(--black)}
  .brand-dark .brand-name{left:0;right:0;top:108px;--s:21px}
  .stamp-photo{left:754px;top:0;width:328px;height:240px;
    background:linear-gradient(110deg,var(--kraft) 0 34%,#f4f4f4 34% 100%)}

  /* Letterhead */
  .letterhead{left:117px;top:314px;width:507px;height:718px;background:var(--paper);font-size:5.5px;color:var(--muted)}
  .letterhead .brand-name{left:58px;top:108px;--s:9px}
  .contact-block{position:absolute;left:58px;top:178px;line-height:1.5}
  .contact-block b{color:var(--ink);font-weight:700}
  .salutation{position:absolute;left:58px;right:58px;top:267px;display:flex;justify-content:space-between;font-size:8px;color:var(--ink)}
  .body-copy{position:absolute;left:58px;right:58px;top:302px;font-size:7.4px;line-height:1.38;text-align:justify}
  .body-copy p{margin-bottom:11px}
  .body-copy p.lead{color:#444}
  .signature{position:absolute;left:62px;top:538px;width:90px;height:30px;background:linear-gradient(90deg,#e6e9f6,#ccd3ef)}
  .signature-rule{position:absolute;left:62px;top:568px;width:92px;height:1px;background:var(--rule)}
  .signer{position:absolute;left:58px;top:578px;font-size:8px;color:var(--ink);line-height:1.3}
  .signer small{display:block;font-size:6px}

  /* Business cards */
  .card-front{left:601px;top:345px;width:233px;height:132px;background:var(--charcoal)}
  .card-front .brand-name{left:0;right:0;top:75px;--s:10.5px}
  .card-back{left:604px;top:502px;width:234px;height:135px;background:var(--paper);font-family:"Bodoni Moda",serif}
  .card-back .brand-name{left:0;right:0;top:33px;--s:6px}
  .card-back .rule{position:absolute;left:36px;right:38px;height:1px;background:var(--rule)}
  .card-back .person{position:absolute;left:0;right:0;top:62px;text-align:center;font-size:6px;text-transform:uppercase;letter-spacing:.04em}
  .card-back .person small{display:block;font-size:4px}
  .card-back .details{position:absolute;top:94px;font-size:4.2px;line-height:1.7;color:var(--muted);white-space:nowrap}
  .card-back .details.left{right:120px;text-align:right}
  .card-back .details.right{left:122px}
  .card-back .divider{position:absolute;left:117px;top:94px;width:1px;height:16px;background:var(--ink)}

  /* Envelopes */
  .envelope-back{left:602px;top:706px;width:434px;height:218px;background:var(--paper)}
  .envelope-back .flap{position:absolute;left:0;top:0;width:434px;height:72px;background:var(--charcoal);border-radius:0 0 10px 10px}
  .envelope-back .flap-rule{position:absolute;top:36px;height:1px;background:#8a8a8a}
  .envelope-back .brand-name{left:0;right:0;top:29px;--s:12px}
  .envelope-front{left:666px;top:836px;width:434px;height:218px;background:var(--paper);border-top:4px solid var(--charcoal)}
  .envelope-front .brand-name{left:38px;top:76px;--s:10px}
  .envelope-front .addr{position:absolute;left:36px;top:124px;font-family:"Bodoni Moda",serif;font-size:8px;letter-spacing:.1em;line-height:1.5;color:#555;list-style:none}
  .envelope-front .addr li{display:flex;gap:5px;align-items:flex-start}
  .envelope-front .addr svg{width:7px;height:7px;margin-top:2px;flex:none}
  .envelope-front .window{position:absolute;left:260px;top:108px;width:142px;height:66px;background:var(--black);border-radius:10px}
</style>
</head>
<body>

  <div class="brand-name brand-light">Delvin &amp; Associates</div>

  <section class="piece brand-dark">
    <div class="brand-name on-dark">Delvin &amp; Associates</div>
  </section>

  <div class="piece stamp-photo" role="img" aria-label="Photo of a wooden rubber stamp on kraft board beside a stamped sheet"></div>

  <section class="piece letterhead">
    <div class="brand-name">Delvin &amp; Associates</div>
    <div class="contact-block">
      <div><b>Phone :</b> (+020) 555 0142</div>
      <div><b>Email :</b> info@delvinassociates.com</div>
      <div><b>Web address :</b> www.delvinassociates.com</div>
      <div><b>Address :</b> 27 Harlow Row, London<br><span style="padding-left:24px">EC2A 4PN</span></div>
    </div>
    <div class="salutation"><span>Dear, Mr________</span><span>Date : ________</span></div>
    <div class="body-copy">
      <p>Lorem Ipsum is simply dummy text of the printing and typesetting industry. Lorem Ipsum has been the industry's standard dummy text ever since the 1500s, when an unknown printer took a galley of type and scrambled it to make a type specimen book. It has survived not only five centuries, but also the leap into electronic typesetting, remaining essentially unchanged. It was popularised in the 1960s with the release of Letraset sheets containing Lorem Ipsum passages, and more recently with desktop publishing software including versions of Lorem Ipsum.</p>
      <p class="lead">Lorem Ipsum is simply dummy text of the printing and typesetting industry. Lorem Ipsum has been the industry's standard dummy text ever since the 1500s, when an unknown printer took a galley of type and scrambled it to make a type specimen book.</p>
      <p>Lorem Ipsum is simply dummy text of the printing and typesetting industry. Lorem Ipsum has been the industry's standard dummy text ever since the 1500s, when an unknown printer took a galley of type and scrambled it to make a type specimen book. It has survived not only five centuries, but also the leap into electronic typesetting, remaining essentially unchanged.</p>
      <p style="margin-top:22px">Lorem Ipsum is simply dummy text of the printing and typesetting industry.</p>
    </div>
    <div class="signature" role="img" aria-label="Handwritten signature"></div>
    <div class="signature-rule"></div>
    <div class="signer">Your Name<small>Designation</small></div>
  </section>

  <section class="piece card-front">
    <div class="brand-name on-dark">Delvin &amp; Associates</div>
  </section>

  <section class="piece card-back">
    <div class="brand-name">Delvin &amp; Associates</div>
    <div class="rule" style="top:55px"></div>
    <div class="person">Your Name<small>Designation</small></div>
    <div class="rule" style="top:83px"></div>
    <div class="details left">(+020) 555 0142 &#9990;<br>info@delvinassociates.com &#9993;</div>
    <div class="divider"></div>
    <div class="details right">www.delvinassociates.com<br>27 Harlow Row, London<br>EC2A 4PN</div>
  </section>

  <section class="piece envelope-back">
    <div class="flap"></div>
    <div class="flap-rule" style="left:0;width:145px"></div>
    <div class="flap-rule" style="right:0;width:145px"></div>
    <div class="brand-name on-dark">Delvin &amp; Associates</div>
  </section>

  <section class="piece envelope-front">
    <div class="brand-name">Delvin &amp; Associates</div>
    <ul class="addr">
      <li><svg viewBox="0 0 10 10"><path d="M2 1l2 2-1 1.5c.8 1.5 1.5 2.2 3 3L7.5 6l2 2-1.5 1.5C4 9 1 6 .5 2z" fill="#222"/></svg>(+020) 555 0142</li>
      <li><svg viewBox="0 0 10 10"><rect x="0" y="2" width="10" height="6.5" fill="#222"/><path d="M0 2l5 4 5-4" stroke="#fff" fill="none"/></svg>info@delvinassociates.com</li>
      <li><svg viewBox="0 0 10 10"><circle cx="5" cy="5" r="4.5" fill="#222"/><path d="M.5 5h9M5 .5c-2 2.5-2 6.5 0 9M5 .5c2 2.5 2 6.5 0 9" stroke="#fff" stroke-width=".7" fill="none"/></svg>www.delvinassociates.com</li>
      <li><svg viewBox="0 0 10 10"><path d="M5 10C2 6 1.5 5 1.5 3.5a3.5 3.5 0 017 0C8.5 5 8 6 5 10z" fill="#222"/><circle cx="5" cy="3.5" r="1.2" fill="#fff"/></svg>27 Harlow Row, London,<br>EC2A 4PN</li>
    </ul>
    <div class="window"></div>
  </section>

</body>
</html>
```